Infographic for Anesthesia Management Company

I would like my Anesthesia Management company, Verity Sedation, service information placed into a infographic for use on a brochure and webpage. Please focus on just the infographic.
-Verity Services text to be placed into infographic attached in word file.
-Two Vector infographic templates attached as well. I am open to either option, or alternative layout suggestion.
-Please match color scheme to veritysedation.com
-Verity logo attached.
Thank you for your help!
Todd
Target Market(s)
Surgery Centers
Industry/Entity Type
It Company
Font styles to use
Requirements
Must have
- Professional Look.
- Easy to read text.
- Cohesive branding
Nice to have
- Please see attached Vector examples.

```html
<!DOCTYPE html>
<html lang="en">
<head>
<meta charset="utf-8">
<title>Verity Sedation – Anesthesia Provider Recruitment, Credentialing, and Staffing</title>
<link rel="stylesheet" href="https://fonts.googleapis.com/css2?family=Lato:wght@900&family=Exo+2:wght@400;500;700&family=Arimo:wght@400;700&display=swap">
<style>
  :root {
    --header-purple: #857199;
    --gold: #c4a832;
    --plum: #88739a;
    --lime: #b8d34f;
    --teal: #15b89f;
    --ink: #161616;
    --white: #ffffff;
    --frame: #e4e4e4;
    --sub-gold: #ffffff;
  }
  * { box-sizing: border-box; margin: 0; padding: 0; }
  html, body { width: 1200px; height: 728px; overflow: hidden; background: var(--white); }
  .canvas { position: relative; width: 1200px; height: 728px; background: var(--white); font-family: "Arimo", Arial, sans-serif; color: var(--ink); }
  .masthead { position: absolute; left: 0; top: 0; width: 1200px; height: 148px; background: var(--header-purple); display: flex; align-items: center; justify-content: center; }
  .masthead h1 { font-family: "Lato", sans-serif; font-weight: 900; color: var(--white); font-size: 43px; line-height: 51px; text-align: center; letter-spacing: 0.5px; }
  .frame { position: absolute; left: 26px; top: 152px; width: 1144px; height: 559px; border-radius: 6px 6px 22px 22px; box-shadow: 0 0 6px rgba(0,0,0,0.12); }
  .panel { position: absolute; }
  .panel--professionalism { left: 30px; top: 157px; width: 392px; height: 297px; background: var(--gold); }
  .panel--accountability { left: 434px; top: 157px; width: 392px; height: 297px; background: var(--plum); }
  .panel--efficiency { left: 836px; top: 157px; width: 330px; height: 297px; background: var(--lime); }
  .panel--safety { left: 30px; top: 462px; width: 780px; height: 245px; background: var(--teal); border-radius: 0 0 0 20px; }
  .panel--contact { left: 810px; top: 462px; width: 356px; height: 245px; background: var(--white); border-radius: 0 0 20px 0; }
  .connector { position: absolute; top: 282px; }
  .el { position: absolute; }
  .heading { font-family: "Exo 2", sans-serif; font-weight: 700; font-size: 29px; line-height: 34px; color: var(--ink); letter-spacing: 0.5px; }
  .subheading { font-family: "Exo 2", sans-serif; font-weight: 500; font-size: 19.5px; line-height: 24px; color: var(--white); }
  .rule { position: absolute; height: 0; border-top: 1px dashed rgba(255,255,255,0.85); }
  .point { position: absolute; display: flex; align-items: flex-start; gap: 0; }
  .point svg { position: absolute; left: 0; }
  .point p { font-size: 13px; line-height: 16.5px; color: var(--ink); }
  .panel--accountability .point p, .panel--safety .point p { color: var(--white); }
  .panel--accountability .point p, .panel--safety .point p { color: #fff; }
  .icon-placeholder { position: absolute; border-radius: 10px; background: linear-gradient(135deg, rgba(255,255,255,0.55), rgba(255,255,255,0.3)); }
  .brand-name { position: absolute; left: 0; width: 356px; top: 44px; text-align: center; font-family: "Exo 2", sans-serif; font-weight: 700; font-size: 38px; color: var(--teal); letter-spacing: 0.5px; }
  .phone { position: absolute; left: 0; width: 356px; top: 118px; text-align: center; font-family: "Exo 2", sans-serif; font-weight: 500; font-size: 46px; line-height: 54px; color: var(--header-purple); }
  .web { position: absolute; left: 0; width: 356px; top: 170px; text-align: center; font-family: "Exo 2", sans-serif; font-weight: 500; font-size: 21px; color: var(--ink); }
  .email { position: absolute; left: 0; width: 356px; top: 197px; text-align: center; font-family: "Exo 2", sans-serif; font-weight: 500; font-size: 15.5px; color: var(--ink); }
</style>
</head>
<body>
<main class="canvas">
  <header class="masthead">
    <h1>ANESTHESIA PROVIDER RECRUITMENT,<br>CREDENTIALING, AND STAFFING</h1>
  </header>

  <div class="frame"></div>

  <!-- Professionalism -->
  <section class="panel panel--professionalism">
    <div class="icon-placeholder" role="img" aria-label="Handshake icon" style="left:14px;top:25px;width:88px;height:58px;"></div>
    <h2 class="heading el" style="left:109px;top:25px;">PROFESSIONALISM</h2>
    <p class="subheading el" style="left:109px;top:66px;color:#fff;">ASC Stakeholder Satisfaction</p>
    <div class="rule" style="left:64px;top:100px;width:306px;"></div>
    <div class="point" style="left:81px;top:121px;">
      <svg width="18" height="18" viewBox="0 0 18 18" style="top:7px"><circle cx="9" cy="9" r="8" fill="none" stroke="#fff" stroke-width="1.8"/><path d="M5 9.2l2.8 2.7L13 6.5" fill="none" stroke="#fff" stroke-width="2"/></svg>
      <p style="margin-left:23px">Share our personal network of highly<br>qualified anesthesia providers</p>
    </div>
    <div class="point" style="left:81px;top:167px;">
      <svg width="18" height="18" viewBox="0 0 18 18" style="top:7px"><circle cx="9" cy="9" r="8" fill="none" stroke="#fff" stroke-width="1.8"/><path d="M5 9.2l2.8 2.7L13 6.5" fill="none" stroke="#fff" stroke-width="2"/></svg>
      <p style="margin-left:23px">Create continuity between anesthesia,<br>surgeon, and ASC staff</p>
    </div>
    <div class="point" style="left:81px;top:213px;">
      <svg width="18" height="18" viewBox="0 0 18 18" style="top:7px"><circle cx="9" cy="9" r="8" fill="none" stroke="#fff" stroke-width="1.8"/><path d="M5 9.2l2.8 2.7L13 6.5" fill="none" stroke="#fff" stroke-width="2"/></svg>
      <p style="margin-left:23px">Guarantee every anesthesia provider<br>upholds clinical excellence</p>
    </div>
    <div class="point" style="left:81px;top:257px;">
      <svg width="18" height="18" viewBox="0 0 18 18" style="top:7px"><circle cx="9" cy="9" r="8" fill="none" stroke="#fff" stroke-width="1.8"/><path d="M5 9.2l2.8 2.7L13 6.5" fill="none" stroke="#fff" stroke-width="2"/></svg>
      <p style="margin-left:23px">Coordinate staffing to meet your<br>scheduled case volume</p>
    </div>
  </section>

  <svg class="connector" style="left:422px;" width="34" height="50" viewBox="0 0 34 50"><path d="M0 0 L26 25 L0 50 L0 42 L18 25 L0 8 Z" fill="#e7e7e7"/><path d="M0 8 L18 25 L0 42 Z" fill="var(--gold)"/></svg>

  <!-- Accountability -->
  <section class="panel panel--accountability">
    <svg class="el" style="left:28px;top:14px;" width="66" height="92" viewBox="0 0 66 92" aria-hidden="true">
      <rect x="3" y="10" width="52" height="76" rx="4" fill="none" stroke="#fff" stroke-width="3.5"/>
      <rect x="17" y="3" width="24" height="12" rx="3" fill="#fff"/>
      <g stroke="#fff" stroke-width="3" fill="none">
        <path d="M10 28l3 3 5-6"/><path d="M24 29h22"/>
        <path d="M10 43l3 3 5-6"/><path d="M24 44h22"/>
        <path d="M10 58l3 3 5-6"/><path d="M24 59h12"/>
        <path d="M10 73l3 3 5-6"/><path d="M24 74h8"/>
      </g>
      <circle cx="48" cy="74" r="15" fill="#fff"/>
      <path d="M41 74l5 5 9-10" fill="none" stroke="var(--plum)" stroke-width="3.5"/>
    </svg>
    <h2 class="heading el" style="left:118px;top:25px;">ACCOUNTABILITY</h2>
    <p class="subheading el" style="left:118px;top:65px;">Meeting Accreditation<br>Requirements</p>
    <div class="rule" style="left:54px;top:127px;width:282px;"></div>
    <div class="point" style="left:62px;top:137px;">
      <svg width="18" height="18" viewBox="0 0 18 18" style="top:2px"><circle cx="9" cy="9" r="8" fill="none" stroke="#fff" stroke-width="1.8"/><path d="M5 9.2l2.8 2.7L13 6.5" fill="none" stroke="#fff" stroke-width="2"/></svg>
      <p style="margin-left:22px">Partner with your surgery center to ensure<br>anesthesia policies and procedures are up<br>to current ASC credentialing standards</p>
    </div>
    <p class="subheading el" style="left:88px;top:196px;">In-House Billing</p>
    <div class="rule" style="left:46px;top:229px;width:284px;"></div>
    <div class="point" style="left:62px;top:235px;">
      <svg width="18" height="18" viewBox="0 0 18 18" style="top:9px"><circle cx="9" cy="9" r="8" fill="none" stroke="#fff" stroke-width="1.8"/><path d="M5 9.2l2.8 2.7L13 6.5" fill="none" stroke="#fff" stroke-width="2"/></svg>
      <p style="margin-left:22px">Dedicated in-house billers ensure<br>anesthesia billing is processed correctly<br>the first time</p>
    </div>
  </section>

  <svg class="connector" style="left:826px;" width="34" height="50" viewBox="0 0 34 50"><path d="M0 0 L26 25 L0 50 L0 42 L18 25 L0 8 Z" fill="#e7e7e7"/><path d="M0 8 L18 25 L0 42 Z" fill="var(--plum)"/></svg>

  <!-- Efficiency -->
  <section class="panel panel--efficiency">
    <svg class="el" style="left:14px;top:15px;" width="84" height="86" viewBox="0 0 84 86" aria-hidden="true">
      <circle cx="36" cy="50" r="30" fill="none" stroke="#fff" stroke-width="7"/>
      <circle cx="36" cy="50" r="17" fill="none" stroke="#fff" stroke-width="6"/>
      <circle cx="36" cy="50" r="6" fill="#fff"/>
      <path d="M36 50 L70 16" stroke="var(--lime)" stroke-width="9"/>
      <path d="M36 50 L70 16" stroke="#fff" stroke-width="4"/>
      <path d="M62 14 L74 2 L76 10 L84 12 L72 24 Z" fill="#fff"/>
    </svg>
    <h2 class="heading el" style="left:105px;top:44px;">EFFICIENCY</h2>
    <p class="subheading el" style="left:100px;top:81px;">Thought Leadership</p>
    <div class="rule" style="left:54px;top:117px;width:224px;"></div>
    <div class="point" style="left:82px;top:131px;">
      <svg width="18" height="18" viewBox="0 0 18 18" style="top:1px"><circle cx="9" cy="9" r="8" fill="none" stroke="#fff" stroke-width="1.8"/><path d="M5 9.2l2.8 2.7L13 6.5" fill="none" stroke="#fff" stroke-width="2"/></svg>
      <p style="margin-left:23px">Stipend free anesthesia<br>services</p>
    </div>
    <div class="point" style="left:82px;top:177px;">
      <svg width="18" height="18" viewBox="0 0 18 18" style="top:1px"><circle cx="9" cy="9" r="8" fill="none" stroke="#fff" stroke-width="1.8"/><path d="M5 9.2l2.8 2.7L13 6.5" fill="none" stroke="#fff" stroke-width="2"/></svg>
      <p style="margin-left:23px">Proprietary and data-driven<br>process to maintain on-time<br>surgery flow</p>
    </div>
  </section>

  <!-- Patient Safety -->
  <section class="panel panel--safety">
    <svg class="el" style="left:22px;top:28px;" width="92" height="90" viewBox="0 0 92 90" aria-hidden="true">
      <path d="M46 62 C20 44 14 32 14 22 C14 10 24 3 33 3 C39 3 43 6 46 10 C49 6 53 3 59 3 C68 3 78 10 78 22 C78 32 72 44 46 62 Z" fill="#fff"/>
      <path d="M20 30 H36 L40 21 L46 40 L51 26 L55 30 H72" fill="none" stroke="var(--teal)" stroke-width="3"/>
      <path d="M4 40 C2 58 12 70 26 78 L30 88 H40 V70 C34 62 26 58 18 50 C14 46 10 42 4 40 Z" fill="#fff"/>
      <path d="M88 40 C90 58 80 70 66 78 L62 88 H52 V70 C58 62 66 58 74 50 C78 46 82 42 88 40 Z" fill="#fff"/>
    </svg>
    <h2 class="heading el" style="left:138px;top:37px;line-height:34px;">PATIENT<br>SAFETY</h2>
    <p class="subheading el" style="left:138px;top:111px;font-weight:400;font-size:21px;line-height:24px;">Clinical Guidance and<br>Quality Improvement</p>
    <div class="point" style="left:362px;top:42px;">
      <svg width="18" height="18" viewBox="0 0 18 18" style="top:7px"><circle cx="9" cy="9" r="8" fill="none" stroke="#fff" stroke-width="1.8"/><path d="M5 9.2l2.8 2.7L13 6.5" fill="none" stroke="#fff" stroke-width="2"/></svg>
      <p style="margin-left:35px">Pre-operative protocols to minimize cancellations<br>and optimize patient outcomes</p>
    </div>
    <div class="point" style="left:362px;top:89px;">
      <svg width="18" height="18" viewBox="0 0 18 18" style="top:7px"><circle cx="9" cy="9" r="8" fill="none" stroke="#fff" stroke-width="1.8"/><path d="M5 9.2l2.8 2.7L13 6.5" fill="none" stroke="#fff" stroke-width="2"/></svg>
      <p style="margin-left:35px">Patient selection criteria to ensure suitable<br>surgical candidates</p>
    </div>
    <div class="point" style="left:362px;top:136px;">
      <svg width="18" height="18" viewBox="0 0 18 18" style="top:7px"><circle cx="9" cy="9" r="8" fill="none" stroke="#fff" stroke-width="1.8"/><path d="M5 9.2l2.8 2.7L13 6.5" fill="none" stroke="#fff" stroke-width="2"/></svg>
      <p style="margin-left:35px">Education programs to engage the clinical<br>staff</p>
    </div>
    <div class="point" style="left:362px;top:179px;">
      <svg width="18" height="18" viewBox="0 0 18 18" style="top:7px"><circle cx="9" cy="9" r="8" fill="none" stroke="#fff" stroke-width="1.8"/><path d="M5 9.2l2.8 2.7L13 6.5" fill="none" stroke="#fff" stroke-width="2"/></svg>
      <p style="margin-left:35px">Evidence based multimodal pain management protocol to<br>facilitate a timely discharge and reduce patient side effects</p>
    </div>
  </section>

  <!-- Contact -->
  <section class="panel panel--contact">
    <p class="brand-name">Verity Sedation</p>
    <p class="phone">(555) 014-2277</p>
    <p class="web">www.veritysedation.com</p>
    <p class="email">toddb@veritysedation.com</p>
  </section>
</main>
</body>
</html>
```